Ashgrove Orthopaedic logo and letterhead

Letterhead AND LOGO rediesign for a surgical medical practice located in Australia.
LOGO - should have an upper limb, shoulder, joint or convey movement
General feel is business/professional. Layout should allow as much space for text as possible
Include the information that is on the proof below that is the current letter head
Need designs in .dotx template and .pdf

Target Market(s)

general practitioner doctors

Industry/Entity Type

medical

Font styles to use
Sans Serif

Colors
0054AA
0677BA
7BADD7
CADEEF
E8F1F8

```html
<!DOCTYPE html>
<html lang="en">
<head>
<meta charset="utf-8">
<title>Ashgrove Orthopaedic Letterhead</title>
<link rel="stylesheet" href="https://fonts.googleapis.com/css2?family=Lato:wght@400;700&family=Mulish:wght@400;700;800&family=Great+Vibes&display=swap">
<style>
  :root {
    --blue-deep: #0054AA;
    --blue-mid: #0677BA;
    --blue-soft: #7BADD7;
    --blue-pale: #CADEEF;
    --blue-mist: #EEF1F8;
    --ink: #2b2b2b;
    --backdrop: #e4e4e4;
    --paper: #ffffff;
  }
  * { box-sizing: border-box; margin: 0; padding: 0; }
  html, body { width: 1153px; height: 1200px; overflow: hidden; background: var(--backdrop); }
  .letterhead {
    position: absolute; left: 167px; top: 20px;
    width: 819px; height: 1160px;
    background: var(--paper); overflow: hidden;
    font-family: "Lato", sans-serif; color: var(--ink);
  }
  .header-wave { position: absolute; left: 0; top: 0; width: 819px; height: 150px; }
  .practitioner {
    position: absolute; right: 58px; top: 27px; text-align: right; color: #fff;
    font-family: "Mulish", sans-serif;
  }
  .practitioner-name { font-size: 19px; font-weight: 800; letter-spacing: 0.1px; }
  .practitioner-role { font-size: 13px; font-weight: 400; margin-top: 2px; }
  .brand-mark {
    position: absolute; left: 62px; top: 74px; width: 78px; height: 78px;
    border: 8px solid var(--blue-deep); border-radius: 50%;
  }
  .brand-name {
    position: absolute; left: 152px; top: 82px;
    font-family: "Lato", sans-serif; font-weight: 700; font-size: 24px; line-height: 26px;
    color: var(--blue-deep); letter-spacing: 0.5px;
  }
  .watermark-ring {
    position: absolute; left: 470px; top: 682px; width: 352px; height: 352px;
    border: 30px solid var(--blue-mist); border-radius: 50%;
  }
  .letter-body {
    position: absolute; left: 80px; top: 252px; width: 671px;
    font-size: 15.5px; line-height: 18.7px;
  }
  .letter-date { margin-bottom: 19px; }
  .recipient { margin-bottom: 19px; }
  .salutation { font-size: 19px; font-weight: 700; color: #333; margin: 12px 0 22px; }
  .letter-paragraph { text-align: justify; font-size: 16px; line-height: 17.7px; letter-spacing: 0.15px; margin-bottom: 17.5px; }
  .closing { margin-top: 40px; }
  .signature { font-family: "Great Vibes", cursive; font-size: 40px; line-height: 1; margin-top: 22px; color: #222; }
  .footer-address {
    position: absolute; left: 49px; top: 1086px; font-family: "Mulish", sans-serif; font-size: 15px;
  }
  .footer-bands { position: absolute; left: 0; top: 1111px; width: 819px; height: 49px; }
  .footer-contact {
    position: absolute; left: 49px; top: 1126px; font-family: "Mulish", sans-serif; font-size: 14.5px; color: #1d1d1d;
  }
  .footer-contact b { font-weight: 800; }
  .footer-notice {
    position: absolute; left: 534px; top: 1121px; font-family: "Mulish", sans-serif;
    font-size: 14.5px; font-weight: 800; color: #fff;
  }
</style>
</head>
<body>
<main class="letterhead">
  <svg class="header-wave" viewBox="0 0 1092 200" preserveAspectRatio="none" aria-hidden="true">
    <path fill="var(--blue-soft)" d="M0,70 C160,15 330,25 520,80 C700,130 820,145 900,145 C700,150 520,120 360,85 C210,55 100,75 0,122 Z"/>
    <path fill="var(--blue-mid)" d="M330,78 C560,110 760,170 900,160 C980,155 1040,140 1092,118 V160 C1000,180 900,178 760,162 C600,140 460,100 330,78 Z"/>
    <path fill="var(--blue-deep)" d="M0,0 H1092 V104 C1000,140 900,140 780,122 C650,100 560,75 480,55 C330,18 150,18 0,70 Z"/>
  </svg>
  <div class="practitioner">
    <div class="practitioner-name">Dr. Daniel Harcourt MBBS FRACS</div>
    <div class="practitioner-role">Orthopaedic Surgeon 458201KT</div>
  </div>
  <div class="brand-mark" aria-hidden="true"></div>
  <div class="brand-name">ASHGROVE<br>ORTHOPAEDIC</div>

  <div class="watermark-ring" aria-hidden="true"></div>

  <section class="letter-body">
    <p class="letter-date">October-01-2023</p>
    <p class="recipient">Mr, John Doe<br>President</p>
    <p class="recipient">Link Corporation<br>123 Street Name, Suite# 10<br>City, State, 120023</p>
    <p class="salutation">Dear Mr, John</p>
    <p class="letter-paragraph">Lorem ipsum dolor sit amet, consectetur adipisicing elit, sed do eiusmod tempor incididunt ut labore et dolore magna aliqua. Ut enim ad minim veniam, quis nostrud exercitation ullamco laboris nisi ut aliquip ex ea commodo consequat. Duis aute irure dolor in reprehenderit in voluptate velit esse cillum dolore eu fugiat nulla pariatur.</p>
    <p class="letter-paragraph">Lorem ipsum dolor sit amet, consectetur adipisicing elit, sed do eiusmod tempor incididunt ut labore et dolore magna aliqua. Ut enim ad minim veniam, quis nostrud exercitation ullamco laboris nisi ut aliquip ex ea commodo consequat. Duis aute irure dolor in reprehenderit in voluptate velit esse cillum dolore eu fugiat nulla pariatur.</p>
    <p class="letter-paragraph">Lorem ipsum dolor sit amet, consectetur adipisicing elit, sed do eiusmod tempor incididunt ut labore et dolore magna aliqua. Ut enim ad minim veniam, quis nostrud exercitation ullamco laboris nisi ut aliquip ex ea commodo consequat.</p>
    <p class="letter-paragraph">Excepteur sint occaecat cupidatat non proident, sunt in culpa qui officia deserunt mollit anim id est laborum. re et dolore magnam aliquam quaerat voluptatem.</p>
    <p class="letter-paragraph">Lorem ipsum dolor sit amet, consectetur adipisicing elit, sed do eiusmod tempor incididunt ut labore et dolore magna aliqua. Ut enim ad minim veniam, quis nostrud exercitation ullamco laboris nisi ut aliquip ex ea commodo consequat.</p>
    <p class="closing">Regards</p>
    <p class="signature">Peter Lawson</p>
  </section>

  <p class="footer-address">Suite 4, Level 2 Eastbrook Private Hospital, Ashgrove 4051</p>
  <svg class="footer-bands" viewBox="0 0 1092 65" preserveAspectRatio="none" aria-hidden="true">
    <polygon fill="var(--blue-deep)" points="0,0 695,0 690,5 0,5"/>
    <polygon fill="var(--blue-soft)" points="0,10 680,10 633,65 0,65"/>
    <polygon fill="var(--blue-deep)" points="708,0 1092,0 1092,65 652,65"/>
  </svg>
  <p class="footer-contact"><b>Ph:</b> 95550142&nbsp; <b>Fax:</b> 85550376&nbsp; <b>E:</b> info@danharcourt.com.au</p>
  <p class="footer-notice">We accept Relay communication</p>
</main>
</body>
</html>
```